Business card with professional look

I would like a creative yet professional looking business card for our business. We sell broadcast TV related security products for mobile phones, set top boxes, and tablets. Our customers are international. We have a logo we like and I would like to possibly add some color to the business card but keep it professional looking.

Target Market(s)

Professionals in the TV, cable, ans Satellite industries

Industry/Entity Type

Cable Tv

Contact Information for Business Card

Name Ted Varnholm, title CEO, Address 1862 Harborline Court, Suite 300, La Jolla, CA 92814 USA, phone numbers m:+1.619.274.3016 o:+1.855.602.1948, email, logo

Font styles to use
Other font styles liked:
• Open to any font that looks good with logo

Requirements
Must have
• professional look with colors coordinated with logo colors. would like to add one or two different colors as well as some form of background color

```html
<!DOCTYPE html>
<html lang="en">
<head>
<meta charset="utf-8">
<title>Vantora Business Card</title>
<link rel="stylesheet" href="https://fonts.googleapis.com/css2?family=Open+Sans:wght@400;600;700;800&display=swap">
<style>
  :root {
    --stage: #141414;
    --card-light: #f3f3f3;
    --brand-blue: #1466b4;
    --blue-deep: #0d56a6;
    --blue-bright: #1c94de;
    --ink: #1c1c1c;
    --logo-grey: #4a4a4a;
    --white: #ffffff;
  }
  * { margin: 0; padding: 0; box-sizing: border-box; }
  html, body {
    width: 1200px;
    height: 900px;
    overflow: hidden;
    background: var(--stage);
    font-family: "Open Sans", Arial, sans-serif;
  }
  .stage {
    position: relative;
    width: 1200px;
    height: 900px;
  }
  .card {
    position: absolute;
    top: 184px;
    width: 302px;
    height: 490px;
    border-radius: 14px;
    overflow: hidden;
  }
  .card-front {
    left: 299px;
    background: var(--card-light);
    text-align: center;
    color: var(--ink);
  }
  .card-back {
    left: 646px;
    width: 304px;
    background: radial-gradient(ellipse at 45% 40%, var(--blue-bright) 0%, #1678c8 45%, var(--blue-deep) 100%);
  }
  .brand-lockup {
    position: absolute;
    top: 76px;
    left: 0;
    right: 0;
    display: flex;
    align-items: center;
    justify-content: center;
    gap: 10px;
  }
  .brand-mark {
    width: 22px;
    height: 22px;
    background: var(--brand-blue);
  }
  .brand-name {
    font-size: 40px;
    font-weight: 700;
    color: var(--logo-grey);
    letter-spacing: -1px;
    line-height: 1;
  }
  .person {
    position: absolute;
    top: 300px;
    left: 0;
    right: 0;
    font-size: 16.5px;
    font-weight: 600;
    color: var(--brand-blue);
  }
  .person .divider { font-weight: 400; margin: 0 2px; }
  .person .role { font-size: 13px; font-weight: 400; }
  .contact {
    position: absolute;
    top: 339px;
    left: 0;
    right: 0;
    list-style: none;
    font-size: 13px;
    line-height: 20px;
  }
  .contact .label { color: var(--brand-blue); font-weight: 700; }
  .address {
    position: absolute;
    top: 416px;
    left: 0;
    right: 0;
    font-size: 13px;
    line-height: 20px;
    font-style: normal;
  }
  .back-name {
    position: absolute;
    left: 32px;
    top: 368px;
    font-size: 62px;
    font-weight: 700;
    color: var(--white);
    letter-spacing: -2px;
    line-height: 1;
  }
</style>
</head>
<body>
<main class="stage">
  <section class="card card-front">
    <div class="brand-lockup">
      <span class="brand-mark"></span>
      <span class="brand-name">Vantora</span>
    </div>
    <p class="person">Ted Varnholm<span class="divider"> |</span><span class="role">CEO</span></p>
    <ul class="contact">
      <li><span class="label">T:</span> +1.619.274.3016</li>
      <li><span class="label">C:</span> +1.855.602.1948</li>
      <li><span class="label">E:</span> info@vantora.com</li>
    </ul>
    <address class="address">1862 Harborline Court, Suite<br>300, La Jolla, CA 92814 USA,</address>
  </section>
  <section class="card card-back">
    <p class="back-name">Vantora</p>
  </section>
</main>
</body>
</html>
```